Decorative concrete business needs new business cards

Our company attracts homeowners and business with disposable cash. We are a artistic decorative coatings company that will transform your driveway, patio, floors or counter tops into a work of art. We also engrave logos and designs right into the concrete! We are upscale and very professional company. I am open for rearranging our logo on the business card and also to different color patterns. We like the blue and black as in BrushNest's logo. We also like blue and orange/yellow.

Target Market(s)

Adults 30-70

Industry/Entity Type

Concrete

Contact Information for Business Card

Simple: Name, phone, email, website and social media icons

Font styles to use
Serif

Colors

Designer to choose colors to be used in the design.

Requirements
Must have
• Must present a professional upscale appearance. I have attached before and after photos that show you what our industry does. Maybe I will have before and after photo on back of card.
Nice to have
• Artistic, but bold. Nothing whimsical or cute.
Should not have
• Should not have cartoon or childlike appearance.

```html
<!DOCTYPE html>
<html lang="en">
<head>
<meta charset="utf-8">
<title>Verano Surface Coatings – Business Card</title>
<link rel="stylesheet" href="https://fonts.googleapis.com/css2?family=Cinzel:wght@400;600&family=Open+Sans:wght@400;600&family=Montserrat:wght@800&display=swap">
<style>
  :root {
    --bg: #2b2b2d;
    --card: #ffffff;
    --brand-blue: #1f7fc0;
    --ink: #333a40;
    --muted: #56606a;
    --chevron: #bcdcee;
    --concrete-before: #c9c7c0;
    --concrete-after: #9a7650;
    --gap: #ffffff;
    --label: #111111;
  }
  * { box-sizing: border-box; margin: 0; padding: 0; }
  html, body { width: 1200px; height: 900px; overflow: hidden; }
  body {
    background: var(--bg);
    display: flex;
    align-items: center;
    justify-content: center;
    gap: 40px;
  }
  .card {
    position: relative;
    width: 540px;
    height: 310px;
    border-radius: 22px;
    overflow: hidden;
    background: var(--card);
  }

  /* Front */
  .card-front__chevrons {
    position: absolute;
    right: 0; top: 0;
    width: 300px; height: 310px;
  }
  .brand {
    position: absolute;
    left: 28px; top: 118px;
    width: 200px;
    display: flex;
    align-items: center;
    gap: 10px;
  }
  .brand__square {
    width: 34px; height: 34px;
    background: var(--brand-blue);
    flex: none;
  }
  .brand__name {
    font-family: "Cinzel", serif;
    font-weight: 600;
    font-size: 17px;
    line-height: 1.05;
    color: var(--brand-blue);
    text-transform: uppercase;
  }
  .divider {
    position: absolute;
    left: 240px; top: 70px;
    width: 1px; height: 170px;
    background: #c9d3da;
  }
  .contact {
    position: absolute;
    left: 256px; top: 68px;
  }
  .contact__name {
    font-family: "Cinzel", serif;
    font-weight: 600;
    font-size: 23px;
    letter-spacing: 0.5px;
    color: var(--brand-blue);
  }
  .contact__title {
    font-family: "Cinzel", serif;
    font-size: 12.5px;
    color: var(--ink);
    margin-bottom: 10px;
  }
  .contact__list { list-style: none; }
  .contact__item {
    display: flex;
    align-items: center;
    gap: 8px;
    font-family: "Open Sans", sans-serif;
    font-size: 13px;
    color: var(--muted);
    line-height: 21px;
  }
  .contact__icon { width: 11px; height: 11px; fill: var(--brand-blue); flex: none; }
  .social {
    display: flex;
    gap: 12px;
    margin-top: 16px;
    margin-left: 32px;
  }
  .social__square {
    width: 17px; height: 17px;
    border-radius: 3px;
    background: var(--brand-blue);
  }

  /* Back */
  .card-back {
    display: grid;
    grid-template-columns: 1fr 1fr;
    grid-template-rows: 1fr 1fr;
    gap: 4px;
    background: var(--gap);
  }
  .photo {
    position: relative;
    display: flex;
    align-items: flex-end;
    justify-content: center;
    padding-bottom: 14px;
  }
  .photo--before { background: linear-gradient(160deg, #8fae8a 0%, #b9b8b0 35%, var(--concrete-before) 100%); }
  .photo--after { background: linear-gradient(160deg, #7f9a6e 0%, #a98457 35%, var(--concrete-after) 100%); }
  .photo__label {
    font-family: "Montserrat", sans-serif;
    font-weight: 800;
    font-size: 15px;
    letter-spacing: 0.5px;
    color: var(--label);
  }
  .photo--after .photo__label { color: #ffffff; }
</style>
</head>
<body>

  <section class="card card-front">
    <svg class="card-front__chevrons" viewBox="0 0 300 310" aria-hidden="true">
      <defs>
        <linearGradient id="chevronFade" x1="1" y1="0" x2="0" y2="1">
          <stop offset="0" stop-color="#bcdcee" stop-opacity="1"/>
          <stop offset="1" stop-color="#bcdcee" stop-opacity="0.2"/>
        </linearGradient>
      </defs>
      <polygon points="80,0 150,0 260,110 300,110 300,150 240,150" fill="url(#chevronFade)"/>
      <polygon points="300,170 240,170 130,310 200,310 270,215 300,215" fill="url(#chevronFade)"/>
      <polygon points="0,0 40,0 230,160 110,310 70,310 180,160" fill="url(#chevronFade)" opacity="0.55"/>
    </svg>

    <div class="brand">
      <span class="brand__square"></span>
      <span class="brand__name">Verano Surface Coatings</span>
    </div>

    <div class="divider"></div>

    <div class="contact">
      <h1 class="contact__name">MARCUS ELLERY</h1>
      <p class="contact__title">General Manager</p>
      <ul class="contact__list">
        <li class="contact__item">
          <svg class="contact__icon" viewBox="0 0 24 24"><path d="M6.6 10.8a15 15 0 0 0 6.6 6.6l2.2-2.2c.3-.3.7-.4 1-.2 1.1.4 2.3.6 3.6.6.6 0 1 .4 1 1V20c0 .6-.4 1-1 1A17 17 0 0 1 3 4c0-.6.4-1 1-1h3.5c.6 0 1 .4 1 1 0 1.3.2 2.5.6 3.6.1.3 0 .7-.2 1z"/></svg>
          0400 555 219
        </li>
        <li class="contact__item">
          <svg class="contact__icon" viewBox="0 0 24 24"><path d="M2 5h20v14H2z M2 5l10 8 10-8" fill="none" stroke="#1f7fc0" stroke-width="3"/></svg>
          info@yourname.com
        </li>
        <li class="contact__item">
          <svg class="contact__icon" viewBox="0 0 24 24"><circle cx="12" cy="12" r="10"/></svg>
          www.websitename.com
        </li>
      </ul>
      <div class="social" aria-label="Social media">
        <span class="social__square"></span>
        <span class="social__square"></span>
        <span class="social__square"></span>
        <span class="social__square"></span>
      </div>
    </div>
  </section>

  <section class="card card-back">
    <div class="photo photo--before" role="img" aria-label="Photo of a plain grey concrete driveway before coating">
      <span class="photo__label">BEFORE</span>
    </div>
    <div class="photo photo--after" role="img" aria-label="Photo of the same driveway after a brown decorative coating">
      <span class="photo__label">AFTER</span>
    </div>
    <div class="photo photo--before" role="img" aria-label="Photo of a cracked concrete driveway in front of garage doors before coating">
      <span class="photo__label">BEFORE</span>
    </div>
    <div class="photo photo--after" role="img" aria-label="Photo of the same garage driveway after a stamped brown coating">
      <span class="photo__label">AFTER</span>
    </div>
  </section>

</body>
</html>
```